Brightwell Estate Stewards, L.L.C
Brightwell Estate Stewards, L.L.C - Financial Services
Creative Brief
Professional
Danielle Whitcombe,CAM
President
P.O. Box 517283 Naples, FL. 34192
info@brightwellestates-example.com
www.brightwellestates-example.com
I am open to clear business cards or two sides if a two sided design is used see comment below.
Logo on back of card if this option is designed

```html
<!DOCTYPE html>
<html lang="en">
<head>
<meta charset="utf-8">
<title>Brightwell Estate Stewards — Stationery Set</title>
<link href="https://fonts.googleapis.com/css2?family=Open+Sans:wght@400;600;700&display=swap" rel="stylesheet">
<style>
  :root{
    --ground:#4b2c20;
    --paper:#ffffff;
    --ink:#6b6b6b;
    --ink-dark:#333333;
    --brand:#0a3aa8;
    --brand-deep:#071a6e;
    --brand-bright:#1f8ff0;
    --cyan:#4ff3ff;
    --clear:rgba(170,140,125,0.55);
  }
  *{margin:0;padding:0;box-sizing:border-box}
  html,body{width:1200px;height:893px;overflow:hidden;background:var(--ground);font-family:"Open Sans",Arial,sans-serif}
  .canvas{position:relative;width:1200px;height:893px}
  .piece{position:absolute;overflow:hidden;background:var(--paper);box-shadow:0 4px 10px rgba(0,0,0,.35)}

  /* brand lockup */
  .mark{position:absolute;display:flex;align-items:center;gap:4px}
  .mark__dot{border-radius:50%;background:var(--brand);flex:none}
  .mark__name{color:var(--brand);font-weight:700;letter-spacing:.02em;white-space:nowrap;text-transform:uppercase}

  .contact{position:absolute;color:var(--ink-dark);line-height:1.35}
  .contact b{color:var(--brand)}

  /* letterhead */
  .letter{width:302px;height:390px;top:56px}
  .letter .mark{left:17px;top:14px}
  .letter .mark__dot{width:26px;height:26px}
  .letter .mark__name{font-size:8.4px}
  .letter .contact{left:188px;top:12px;font-size:6px}
  .letter__body{position:absolute;left:19px;top:87px;width:273px;font-size:4.9px;line-height:6.9px;color:var(--ink)}
  .letter__body p{margin-bottom:7px}
  .letter__body .addr{margin-bottom:7px}
  .letter__sign{position:absolute;left:19px;top:296px;font-size:4.9px;line-height:6.9px;color:var(--ink)}
  .letter__orb{position:absolute;left:211px;top:299px;width:92px;height:92px;border-radius:50%;background:radial-gradient(circle at 45% 40%,var(--brand-bright),var(--brand) 60%,var(--brand-deep))}
  .band{position:absolute;left:0;right:0;bottom:0;height:10px;color:#fff;font-size:6px;line-height:10px;padding-left:15px}
  .band--solid{background:var(--brand)}
  .band--glow{background:linear-gradient(90deg,var(--brand-deep) 0%,var(--brand) 20%,var(--cyan) 38%,var(--brand-bright) 55%,var(--brand-deep) 100%)}

  /* cards */
  .card{width:219px;height:125px;border-radius:9px}
  .card--clear{background:var(--clear)}
  .card .mark{left:16px;top:13px}
  .card .mark__dot{width:24px;height:24px}
  .card .mark__name{font-size:6.4px}
  .card__name{position:absolute;left:17px;top:54px;font-size:9.6px;font-weight:700;color:var(--brand)}
  .card__role{position:absolute;left:17px;top:67px;font-size:5.8px;color:var(--ink-dark)}
  .card .contact{left:17px;top:76px;font-size:5.6px}
  .card__orb{position:absolute;left:138px;top:44px;width:90px;height:90px;border-radius:50%;background:radial-gradient(circle at 45% 40%,var(--brand-bright),var(--brand) 60%,var(--brand-deep))}
  .card .band{height:8px;line-height:8px;font-size:5.4px;padding-left:18px;right:auto;width:100%}
  .card--clear .contact,.card--clear .card__role{color:#fff}

  .card__header{position:absolute;left:0;right:0;top:19px;height:31px;background:linear-gradient(90deg,var(--brand-deep),var(--brand) 55%,var(--brand-bright) 78%,var(--brand-deep));border-top:2px solid #dfe3f0;border-bottom:2px solid #dfe3f0;padding:6px 0 0 15px;color:#fff}
  .card__header strong{display:block;font-size:9.4px;line-height:11px}
  .card__header span{font-size:5.6px}
  .card .mark--stack{left:15px;top:62px;flex-direction:column;gap:3px}
  .card .mark--stack .mark__dot{width:30px;height:30px}
  .card .mark--stack .mark__name{font-size:5.4px}
  .card .contact--side{left:113px;top:73px;font-size:5.6px}

  .card--back{background:radial-gradient(ellipse at 50% 40%,var(--brand-bright),var(--brand) 55%,var(--brand-deep));}
  .card--back .back__dot{position:absolute;left:91px;top:36px;width:44px;height:44px;border-radius:50%;background:#d9dde6}
  .card--back .back__url{position:absolute;left:0;right:0;top:90px;text-align:center;color:#fff;font-size:5.8px}

  /* envelopes */
  .envelope{width:387px;height:169px}
  .envelope .mark{left:21px;top:20px}
  .envelope .mark__dot{width:32px;height:32px}
  .envelope .mark__name{font-size:10.5px}
  .envelope .contact{left:23px;top:62px;font-size:8.2px;color:var(--ink-dark)}
  .envelope .band{height:11px}
  .flap{width:376px;height:166px}
  .flap svg{position:absolute;left:0;top:0}
  .flap__dot{position:absolute;width:40px;height:40px;border-radius:50%;left:168px;top:10px}
</style>
</head>
<body>
<main class="canvas">

  <!-- Letterhead, solid band -->
  <section class="piece letter" style="left:54px">
    <div class="mark"><span class="mark__dot"></span><span class="mark__name">Brightwell Estate Stewards</span></div>
    <div class="contact">P.O. Box 517283<br>Naples, FL 34192<br><b>C:</b> 239.555.0184<br><b>E:</b> info@brightwellestates-example.com</div>
    <div class="letter__body">
      <p class="addr">Someone Somebody<br>24 Harbour Rd<br>Perth, Australia</p>
      <p>Dear Someone Somebody,</p>
      <p>Thank you for your recent inquiry about our community services. We manage associations across the region with care, clear reporting and steady budgets that residents can trust year after year.</p>
      <p>Our team handles maintenance schedules, vendor contracts, board meetings and resident requests. Every property receives a dedicated manager and a monthly summary of finances and open work orders.</p>
      <p>We would welcome the chance to review your current arrangements and suggest practical improvements. A short meeting at your convenience would let us understand your goals in detail.</p>
      <p>Please find our service outline enclosed. Feel free to call or write with any questions, and we look forward to hearing from you soon.</p>
    </div>
    <div class="letter__sign">Your Sincerely,<br>Marcus Ellery.</div>
    <div class="band band--solid">www.brightwellestates-example.com</div>
    <div class="letter__orb" role="img" aria-label="Large brand circle decoration"></div>
  </section>

  <!-- Letterhead, gradient band -->
  <section class="piece letter" style="left:386px;top:54px">
    <div class="mark"><span class="mark__dot"></span><span class="mark__name">Brightwell Estate Stewards</span></div>
    <div class="contact">P.O. Box 517283<br>Naples, FL. 34192<br><b>C:</b> 239.555.0184<br><b>E:</b> info@brightwellestates-example.com</div>
    <div class="letter__body">
      <p class="addr">Someone Somebody<br>24 Harbour Rd<br>Perth, Australia</p>
      <p>Dear Someone Somebody,</p>
      <p>Thank you for your recent inquiry about our community services. We manage associations across the region with care, clear reporting and steady budgets that residents can trust year after year.</p>
      <p>Our team handles maintenance schedules, vendor contracts, board meetings and resident requests. Every property receives a dedicated manager and a monthly summary of finances and open work orders.</p>
      <p>We would welcome the chance to review your current arrangements and suggest practical improvements. A short meeting at your convenience would let us understand your goals in detail.</p>
      <p>Please find our service outline enclosed. Feel free to call or write with any questions, and we look forward to hearing from you soon.</p>
    </div>
    <div class="letter__sign">Your Sincerely,<br>Marcus Ellery.</div>
    <div class="band band--glow">www.brightwellestates-example.com</div>
  </section>

  <!-- Business card, front A -->
  <section class="piece card" style="left:718px;top:54px">
    <div class="mark"><span class="mark__dot"></span><span class="mark__name">Brightwell Estate Stewards</span></div>
    <div class="card__name">Danielle Whitcombe,CAM</div>
    <div class="card__role">President</div>
    <div class="contact">P.O. Box 517283<br>Naples, FL 34192<br><b>C:</b> 239.555.0184<br><b>E:</b> info@brightwellestates-example.com</div>
    <div class="band band--solid">www.brightwellestates-example.com</div>
    <div class="card__orb" role="img" aria-label="Large brand circle decoration"></div>
  </section>

  <!-- Business card, front B -->
  <section class="piece card" style="left:964px;top:54px">
    <div class="card__header"><strong>Danielle Whitcombe,CAM</strong><span>President</span></div>
    <div class="mark mark--stack"><span class="mark__dot"></span><span class="mark__name">Brightwell Estate Stewards</span></div>
    <div class="contact contact--side">P.O. Box 517283<br>Naples, FL. 34192<br><b>C:</b> 239.555.0184<br><b>E:</b> info@brightwellestates-example.com</div>
  </section>

  <!-- Clear card, front A -->
  <section class="piece card card--clear" style="left:718px;top:200px">
    <div class="mark"><span class="mark__dot"></span><span class="mark__name">Brightwell Estate Stewards</span></div>
    <div class="card__name">Danielle Whitcombe,CAM</div>
    <div class="card__role">President</div>
    <div class="contact">P.O. Box 517283<br>Naples, FL 34192<br><b>C:</b> 239.555.0184<br><b>E:</b> info@brightwellestates-example.com</div>
    <div class="band band--solid">www.brightwellestates-example.com</div>
    <div class="card__orb" role="img" aria-label="Large brand circle decoration"></div>
  </section>

  <!-- Clear card, front B -->
  <section class="piece card card--clear" style="left:964px;top:200px">
    <div class="card__header"><strong>Danielle Whitcombe,CAM</strong><span>President</span></div>
    <div class="mark mark--stack"><span class="mark__dot"></span><span class="mark__name">Brightwell Estate Stewards</span></div>
    <div class="contact contact--side" style="left:117px">P.O. Box 517283<br>Naples, FL 34192<br><b>C:</b> 239.555.0184<br><b>E:</b> info@brightwellestates-example.com</div>
  </section>

  <!-- Card back -->
  <section class="piece card card--back" style="left:827px;top:356px">
    <div class="back__dot"></div>
    <div class="back__url">www.brightwellestates-example.com</div>
  </section>

  <!-- Envelope fronts -->
  <section class="piece envelope" style="left:56px;top:499px">
    <div class="mark"><span class="mark__dot"></span><span class="mark__name">Brightwell Estate Stewards</span></div>
    <div class="contact">P.O. Box 517283<br>Naples, FL. 34192</div>
    <div class="band band--solid"></div>
  </section>

  <section class="piece envelope" style="left:483px;top:499px">
    <div class="mark"><span class="mark__dot"></span><span class="mark__name">Brightwell Estate Stewards</span></div>
    <div class="contact">P.O. Box 517283<br>Naples, FL. 34192</div>
    <div class="band band--glow"></div>
  </section>

  <!-- Envelope backs -->
  <section class="piece flap" style="left:56px;top:699px">
    <svg width="376" height="166" viewBox="0 0 376 166" aria-hidden="true">
      <path d="M0 0 H376 C366 20 360 32 340 38 L200 70 Q188 74 176 70 L40 38 C16 32 8 20 0 0 Z" fill="var(--brand)"/>
    </svg>
    <span class="flap__dot" style="background:var(--brand)"></span>
  </section>

  <section class="piece flap" style="left:485px;top:690px;height:164px">
    <defs></defs>
    <svg width="376" height="164" viewBox="0 0 376 164" aria-hidden="true">
      <defs>
        <linearGradient id="flapGlow" x1="0" x2="1" y1="0" y2="0">
          <stop offset="0" stop-color="#071a6e"/>
          <stop offset=".3" stop-color="#0a3aa8"/>
          <stop offset=".5" stop-color="#4ff3ff"/>
          <stop offset=".7" stop-color="#0a3aa8"/>
          <stop offset="1" stop-color="#071a6e"/>
        </linearGradient>
      </defs>
      <path d="M0 0 H376 C366 24 360 34 340 40 L200 70 Q188 74 176 70 L36 40 C16 34 8 24 0 0 Z" fill="url(#flapGlow)"/>
    </svg>
    <span class="flap__dot" style="background:#d9dde6;top:10px"></span>
  </section>

</main>
</body>
</html>
```